Concert Poster

Dear all!
It seems that we have found our final design!
Thanks a lot for your contribution so far. It is not necessary to post any more designs.

BR Lukas

____________________
For the band Velvet Comet - we would like to have a standard concert announcement poster that we can use to advertise for our gigs.The band plays the classic songs of the disco era end of the 70ies, e.g. Lumo, Carla Brightwood, Silver Moth Parade, Rudy & The Orbits etc. On stage we also adapt to the fashion of those times, but in a modern manner.See more details on our website: www.velvetcomet-band.de

We intend to position the band in the high price segment - so that poster should be positively effective even between posters of famous bands.

Format: DIN-A1 Portrait - 594 x 841 mm

If possible, it would also be great if we could use the same design to print flyers (format DIN-A6).

Target Market(s)

Live Music Bands

Requirements
Must have
• The poster should contain:
• - Our logo (see uploads)
• - Our official photo (see uploads)
• - Text about date, venue, time, entrance fee or the concert AND
• alternatively a possibility to leave this space blank so that we can print a bunch of empty posters that we can write the details on manually (to avoid printing posters for each gig individually)
• - Information about the Band:
• - Website: www.velvetcomet-band.de
• - Like us on facebook: fb/velvetcometband

```html
<!DOCTYPE html>
<html lang="en">
<head>
<meta charset="utf-8">
<title>Velvet Comet – Concert Poster</title>
<link rel="stylesheet" href="https://fonts.googleapis.com/css2?family=Montserrat:wght@400;500;600;700;800&display=swap">
<style>
  :root {
    --night: #0a0c26;
    --deep: #05060f;
    --violet: #3b1f6e;
    --magenta: #a2266a;
    --gold: #f7b84a;
    --gold-light: #fde39a;
    --orange: #f08a45;
    --white: #ffffff;
    --soft: #d9d9e6;
    --photo: #8a8a8f;
  }
  * { margin: 0; padding: 0; box-sizing: border-box; }
  html, body { width: 890px; height: 1200px; overflow: hidden; background: var(--night); }
  body { font-family: "Montserrat", Arial, sans-serif; color: var(--white); }

  .poster {
    position: relative; width: 890px; height: 1200px; overflow: hidden;
    background:
      radial-gradient(ellipse 420px 300px at 50% 380px, rgba(162,38,106,.5), transparent 70%),
      radial-gradient(ellipse 600px 420px at 50% 520px, rgba(59,31,110,.9), transparent 75%),
      linear-gradient(180deg, #0d1033 0%, var(--night) 55%, var(--deep) 80%, var(--deep) 100%);
  }

  .stage-art {
    position: absolute; left: 225px; top: 0; width: 440px; height: 280px;
    background: radial-gradient(closest-side, rgba(253,227,154,.75) 0%, rgba(247,184,74,.55) 30%, rgba(240,138,69,.3) 55%, rgba(162,38,106,.15) 78%, transparent 100%);
  }

  .band-name { position: absolute; left: 0; right: 0; text-align: center; }
  .band-name--top { top: 232px; font-size: 112px; line-height: 116px; font-weight: 800; letter-spacing: 4px; color: var(--gold); }
  .band-name--bottom { top: 362px; font-size: 86px; line-height: 90px; font-weight: 500; letter-spacing: 12px; color: var(--white); }

  .side-stripes { position: absolute; top: 545px; width: 60px; height: 85px; }
  .side-stripes--left { left: 0; }
  .side-stripes--right { right: 0; }
  .side-stripes span { display: block; height: 16px; margin-bottom: 13px; background: linear-gradient(90deg, #fff, #cfcfd8); }

  .lineup { position: absolute; top: 480px; left: 0; width: 890px; height: 290px; }
  .member { position: absolute; top: 0; width: 178px; height: 258px; }
  .member__frame { position: absolute; left: 12px; top: 14px; width: 178px; height: 258px; background: var(--orange); }
  .member__photo { position: absolute; inset: 0; border: 3px solid var(--white); background: linear-gradient(160deg, #b5b5ba, var(--photo) 55%, #3e3e44); }

  .gig { position: absolute; top: 790px; width: 200px; text-align: center; font-size: 13px; line-height: 17px; }
  .gig__date { font-weight: 700; font-size: 15px; margin-bottom: 14px; }
  .gig__venue, .gig__address { font-weight: 500; margin-bottom: 12px; }
  .gig__time { font-weight: 700; font-size: 15px; line-height: 19px; }

  .divider { position: absolute; left: 45px; right: 45px; top: 968px; height: 2px; background: linear-gradient(90deg, transparent, var(--gold) 15%, var(--gold) 85%, transparent); }
  .about-pill {
    position: absolute; left: 315px; top: 956px; width: 260px; height: 26px; border-radius: 13px;
    background: linear-gradient(180deg, var(--gold-light), var(--gold));
    color: #1a1204; font-weight: 800; font-size: 15px; letter-spacing: 2px; text-align: center; line-height: 26px;
  }
  .headline { position: absolute; top: 994px; left: 0; right: 0; text-align: center; font-weight: 700; font-size: 31px; line-height: 40px; letter-spacing: .5px; }
  .info-bar {
    position: absolute; top: 1044px; left: 100px; right: 100px; height: 40px; border: 2px solid var(--gold); border-radius: 20px;
    text-align: center; font-weight: 600; font-size: 19px; line-height: 36px;
  }
  .blurb { position: absolute; top: 1096px; left: 70px; right: 70px; text-align: center; font-size: 12.5px; line-height: 17px; color: var(--soft); }
  .links { position: absolute; top: 1140px; left: 0; right: 0; text-align: center; font-weight: 600; font-size: 13px; letter-spacing: 2.5px; text-transform: uppercase; }
  .links .dot { display: inline-block; width: 5px; height: 5px; border-radius: 50%; background: var(--white); margin: 0 16px; vertical-align: middle; }
</style>
</head>
<body>
<main class="poster">
  <div class="stage-art" role="img" aria-label="Glowing golden disco ball with dancing silhouettes"></div>

  <h1>
    <span class="band-name band-name--top">VELVET</span>
    <span class="band-name band-name--bottom">COMET</span>
  </h1>

  <div class="side-stripes side-stripes--left"><span></span><span></span><span></span></div>
  <div class="side-stripes side-stripes--right"><span></span><span></span><span></span></div>

  <section class="lineup">
    <div class="member" style="left:42px"><div class="member__frame"></div><div class="member__photo" role="img" aria-label="Black and white photo of two band members in sunglasses"></div></div>
    <div class="member" style="left:246px"><div class="member__frame"></div><div class="member__photo" role="img" aria-label="Black and white photo of two singers holding a mirror ball"></div></div>
    <div class="member" style="left:452px"><div class="member__frame"></div><div class="member__photo" role="img" aria-label="Black and white photo of two smiling band members"></div></div>
    <div class="member" style="left:654px"><div class="member__frame"></div><div class="member__photo" role="img" aria-label="Black and white photo of a band member in a patterned shirt"></div></div>
  </section>

  <div class="gig" style="left:32px">
    <p class="gig__date">FRIDAY, 23.11.2018</p>
    <p class="gig__venue">Soundhall Munich</p>
    <p class="gig__address">Lerchenweg 14,<br>80939 Munich</p>
    <p class="gig__time">Start: 20:30,<br>entrance: 20:00</p>
  </div>
  <div class="gig" style="left:235px">
    <p class="gig__date">SUNDAY, 03.03.2019</p>
    <p class="gig__venue">Hotel Lindenhof -<br>Night Club</p>
    <p class="gig__address">Lindenplatz 5,<br>80333 Munich</p>
    <p class="gig__time">Start: 22.00 clock</p>
  </div>
  <div class="gig" style="left:441px">
    <p class="gig__date">MONDAY, 04.03.2019</p>
    <p class="gig__venue">Hotel Lindenhof -<br>Night Club</p>
    <p class="gig__address">Lindenplatz 5,<br>80333 Munich</p>
    <p class="gig__time">Start: 22.00 clock</p>
  </div>
  <div class="gig" style="left:643px">
    <p class="gig__date">TUESDAY, 05.03.2019</p>
    <p class="gig__venue">Hotel Lindenhof -<br>Night Club</p>
    <p class="gig__address">Lindenplatz 5,<br>80333 Munich</p>
    <p class="gig__time">Start: 22.00 clock</p>
  </div>

  <div class="divider"></div>
  <div class="about-pill">ABOUT VELVET COMET</div>
  <h2 class="headline">THE LEGENDARY ERA OF THE 70S AND 80S</h2>
  <div class="info-bar">22.00 CLOCK • €9 ENTRY • HOTEL LINDENHOF - NIGHT CLUB</div>
  <p class="blurb">The band plays the classic songs of the disco era end of the 70ies, e.g. Lumo, Carla Brightwood, Silver Moth Parade, Rudy &amp; The Orbits etc. On stage we also adapt to the fashion of those times, but in a modern manner.</p>
  <p class="links">www.velvetcomet-band.de<span class="dot"></span>fb/velvetcometband</p>
</main>
</body>
</html>
```